100% West Australian Static Banner

I require a static banner to go on a couple of pages in our website (under development) that highlights that we are a 100% Western Australian Owned & Operated company. I would prefer the banner to be in our company colours (blue shades & grey). I also would like it to be eye catching and modern in design. I have included a 100% West Australian rubber stamp logo to be used as well as including our logo so you know our colours. The banner needs to be 1139 x 350 pixels in size.

Target Market(s)

B2B

Requirements
Must have
• Our rubber stamp 100% West Australian logo
• Modern Eye Catching design
• Blue shaded background
Nice to have
• Shading background similar our logo blue colours
• 100% logo can be reversed out if required or colour changed
• Larger text saying - 100% West Australian Owned & Operated

```html
<!DOCTYPE html>
<html lang="en">
<head>
<meta charset="utf-8">
<title>100% West Australian Banner Options</title>
<link rel="stylesheet" href="https://fonts.googleapis.com/css2?family=Montserrat:wght@600;800&family=Fira+Sans:wght@700&display=swap">
<style>
  :root {
    --board: #464646;
    --label: #d6d6d6;
    --blue: #0a58a0;
    --blue-deep: #063a78;
    --grey: #a6a6a6;
    --white: #ffffff;
    --yellow: #f7ea10;
  }
  html, body {
    margin: 0;
    width: 1200px;
    height: 1200px;
    overflow: hidden;
    background: var(--board);
  }
  .board { position: relative; width: 1200px; height: 1200px; }
  .option-label {
    position: absolute;
    left: 151px;
    margin: 0;
    font: 700 16px "Fira Sans", sans-serif;
    color: var(--label);
    letter-spacing: 0.5px;
  }
  .banner {
    position: absolute;
    left: 145px;
    width: 912px;
    height: 278px;
    display: block;
  }
  .headline { font-family: "Montserrat", sans-serif; font-weight: 800; }
  .brand-name { font-family: "Montserrat", sans-serif; font-weight: 600; fill: var(--blue); }
  .fill-white { fill: var(--white); }
  .fill-yellow { fill: var(--yellow); }
  .fill-blue { fill: var(--blue); }
  .fill-grey { fill: var(--grey); }
  .stamp { fill: var(--blue); stroke: var(--white); stroke-width: 10; }
</style>
</head>
<body>
<main class="board">

  <p class="option-label" style="top:64px">OPT 1</p>
  <svg class="banner" style="top:91px" viewBox="0 0 1140 348" aria-label="Banner option 1">
    <defs>
      <linearGradient id="blue-shade" x1="0" y1="0" x2="0" y2="1">
        <stop offset="0.45" stop-color="var(--blue)"/>
        <stop offset="1" stop-color="var(--blue-deep)"/>
      </linearGradient>
    </defs>
    <rect width="1140" height="348" fill="url(#blue-shade)"/>
    <polygon class="fill-grey" points="712,0 1140,0 1140,348 862,348"/>
    <polygon class="fill-white" points="732,0 1140,0 1140,348 880,348"/>
    <g class="brand-mark">
      <rect class="fill-blue" x="795" y="26" width="52" height="52"/>
      <text class="brand-name" x="862" y="66" font-size="30">CoreCrate</text>
    </g>
    <rect class="fill-yellow" x="38" y="110" width="190" height="77" rx="9"/>
    <text class="headline fill-blue" x="133" y="168" font-size="50" text-anchor="middle">100%</text>
    <text class="headline fill-white" x="242" y="168" font-size="47">WEST AUSTRALIAN</text>
    <polyline points="228,186 735,186 735,120" fill="none" stroke="var(--yellow)" stroke-width="2"/>
    <text class="headline fill-white" x="386" y="243" font-size="44" text-anchor="middle">OWNED &amp; OPERATED</text>
    <circle class="stamp" cx="854" cy="244" r="78" role="img" aria-label="100% West Australian owned and operated stamp"/>
  </svg>

  <p class="option-label" style="top:440px">OPT 2</p>
  <svg class="banner" style="top:469px" viewBox="0 0 1140 350" aria-label="Banner option 2">
    <rect width="1140" height="350" class="fill-blue"/>
    <polygon class="fill-white" points="670,0 1140,0 1140,100 761,100"/>
    <polygon class="fill-grey" points="616,350 1140,187 1140,350"/>
    <g class="brand-mark">
      <rect class="fill-blue" x="795" y="25" width="52" height="52"/>
      <text class="brand-name" x="862" y="62" font-size="30">CoreCrate</text>
    </g>
    <text class="headline fill-white" x="295" y="156" font-size="68" text-anchor="end">100%</text>
    <text class="headline fill-yellow" x="295" y="209" font-size="34" text-anchor="end">WEST</text>
    <text class="headline fill-yellow" x="295" y="247" font-size="34" text-anchor="end">AUSTRALIAN</text>
    <line x1="317" y1="92" x2="317" y2="256" stroke="var(--yellow)" stroke-width="2"/>
    <text class="headline fill-white" x="338" y="164" font-size="58">OWNED &amp;</text>
    <text class="headline fill-white" x="338" y="232" font-size="58">OPERATED</text>
    <circle class="stamp" cx="921" cy="247" r="86" role="img" aria-label="100% West Australian owned and operated stamp"/>
  </svg>

  <p class="option-label" style="top:820px">OPT 3</p>
  <svg class="banner" style="top:848px" viewBox="0 0 1140 348" aria-label="Banner option 3">
    <rect width="1140" height="348" class="fill-blue"/>
    <polygon class="fill-white" points="0,0 540,0 0,192"/>
    <polygon class="fill-grey" points="616,348 1140,185 1140,348"/>
    <g class="brand-mark">
      <rect class="fill-blue" x="20" y="24" width="52" height="52"/>
      <text class="brand-name" x="87" y="60" font-size="27">CoreCrate</text>
    </g>
    <g class="tilted-headline" transform="rotate(-12 497 175)">
      <text class="headline fill-white" x="474" y="174" font-size="68" text-anchor="end">100%</text>
      <text class="headline fill-yellow" x="474" y="224" font-size="34" text-anchor="end">WEST</text>
      <text class="headline fill-yellow" x="474" y="262" font-size="34" text-anchor="end">AUSTRALIAN</text>
      <line x1="497" y1="100" x2="497" y2="265" stroke="var(--yellow)" stroke-width="2"/>
      <text class="headline fill-white" x="518" y="172" font-size="58">OWNED &amp;</text>
      <text class="headline fill-white" x="518" y="240" font-size="58">OPERATED</text>
    </g>
    <circle class="stamp" cx="1001" cy="237" r="84" role="img" aria-label="100% West Australian owned and operated stamp"/>
  </svg>

</main>
</body>
</html>
```